New young doctors office business card

Doctor's office
Hello:
My name is Dr. Mateo Anselmo Quiroga Benítez. I need a business card for my new office located within a hospital. The name of the hospital is "Hospital Almendral". Although the hospital logo and name must be included in the business card, please make me a personal logo for myself. The logo might be maybe my name in a stylish font, or my initials (MAQB) or something like that. Im more inclined to a font logo, rather than a image logo, but a good one might change my mind. The info on my business card is going to be in spanish. The following info must be included please (the info within parenthesis is not to be included, it is provided for you to understand it since it's in spanish, so you can properly place it on the card):
-Dr. Mateo Anselmo Quiroga Benítez (my name)
-Medicina general (My specialty)
-Hospital Almendral (The name of the hospital where my office is)
-Calle Tomás Ibarrola #527 Col. Peñascal (address)
-Tel 471-5836 (Office phone)
-Sábado y domingo 10:00 am a 10:00pm (Office hours)
-Emergencias: 613-907-5148 (Emergency phone)
-mateoqb@correoandino.net (email)
-English Spoken
So, that's all the info i need to be on the business card. Although it's a business card for a doctor's office, i dont want it to be a boring, plain business card. Make it eye-catchy and stylish please. As i said, the hospital logo must be included. You'll find it on the heading of the PDF file i attached, but dont make it the center of attention.
Physician
Hello:My name is Dr. Mateo Anselmo Quiroga Benítez. I need a business card for my new office located within a hospital. The name of the hospital is "Hospital Almendral". Although the hospital logo and name must be included in the business card, please make me a personal logo for myself. The logo might be maybe my name in a stylish font, or my initials (MAQB) or something like that. Im more inclined to a font logo, rather than a image logo, but a good one might change my mind. The info on my business card is going to be in spanish. The following info must be included please (the info within parenthesis is not to be included, it is provided for you to understand it since it's in spanish, so you can properly place it on the card):-Dr. Mateo Anselmo Quiroga Benítez (my name)-Medicina general (My specialty)-Hospital Almendral (The name of the hospital where my office is)-Calle Tomás Ibarrola #527 Col. Peñascal (address)-Tel 471-5836 (Office phone)-Sábado y domingo 10:00 am a 10:00pm (Office hours)-Emergencias: 613-907-5148 (Emergency phone)-mateoqb@correoandino.net (email)-English Spoken So, that's all the info i need to be on the business card. Although it's a business card for a doctor's office, i dont want it to be a boring, plain business card. Make it eye-catchy and stylish please. As i said, the hospital logo must be included. You'll find it on the heading of the PDF file i attached, but dont make it the center of attention.

```html
<!DOCTYPE html>
<html lang="es">
<head>
<meta charset="UTF-8">
<title>MAQB – Tarjeta de presentación</title>
<link href="https://fonts.googleapis.com/css2?family=Source+Sans+3:wght@400;600;700&display=swap" rel="stylesheet">
<style>
  :root {
    --backdrop: #1d1512;
    --card-dark: #111010;
    --card-light: #d9dad8;
    --gold-hi: #efe07a;
    --gold-lo: #9a7d14;
    --name-yellow: #d8d51c;
    --silver: #b9bbbd;
    --rule: #9ea3a8;
    --ink: #1b1b1b;
    --hospital-blue: #1b2aa6;
    --hours-orange: #d8541a;
    --soft-white: #e6e6e6;
  }
  * { box-sizing: border-box; margin: 0; padding: 0; }
  html, body {
    width: 1200px; height: 918px; overflow: hidden;
    background: var(--backdrop);
    font-family: "Source Sans 3", sans-serif;
  }
  .card {
    position: absolute; left: 230px;
    width: 740px; height: 423px;
    overflow: hidden;
    box-shadow: 0 14px 30px rgba(0,0,0,.55);
  }

  /* Back side */
  .card--back { top: 22px; background: var(--card-dark); }
  .back__initials {
    position: absolute; left: 330px; top: 95px;
    font-size: 92px; font-weight: 400; letter-spacing: 6px;
    color: var(--silver);
  }
  .back__rule {
    position: absolute; left: 230px; top: 205px;
    width: 360px; height: 2px; background: var(--silver);
  }
  .back__hospital {
    position: absolute; left: 230px; top: 222px;
    display: flex; align-items: center; gap: 12px;
  }
  .back__mark { width: 44px; height: 44px; background: var(--silver); }
  .back__hospital-name { font-size: 34px; font-weight: 700; color: var(--silver); }
  .back__address {
    position: absolute; left: 286px; top: 270px;
    font-size: 17px; color: var(--silver);
  }

  /* Front side */
  .card--front { top: 473px; background: var(--card-light); }
  .front__band {
    position: absolute; left: 0; top: 0; width: 100%; height: 186px;
    background: var(--card-dark);
  }
  .front__initials {
    position: absolute; left: 42px; top: 22px;
    font-size: 84px; font-weight: 400; letter-spacing: 5px;
    background: linear-gradient(180deg, var(--gold-hi), var(--gold-lo) 70%, #6f5a0c);
    -webkit-background-clip: text; background-clip: text; color: transparent;
  }
  .front__rule {
    position: absolute; left: 250px; top: 118px;
    width: 462px; height: 3px; background: var(--rule);
  }
  .front__name {
    position: absolute; right: 28px; top: 76px;
    font-size: 25px; font-weight: 600; color: var(--name-yellow);
  }
  .front__specialty {
    position: absolute; right: 28px; top: 130px;
    font-size: 24px; color: var(--soft-white);
  }
  .contact {
    position: absolute; left: 220px; top: 203px;
    font-size: 20px; color: var(--ink); line-height: 30px;
  }
  .contact__row { display: flex; align-items: center; gap: 12px; }
  .contact__icon {
    width: 32px; height: 32px; background: var(--card-dark);
    display: flex; align-items: center; justify-content: center;
  }
  .contact__label { display: inline-block; width: 112px; }
  .hospital {
    position: absolute; left: 30px; top: 312px;
    display: flex; align-items: center; gap: 12px;
  }
  .hospital__mark { width: 52px; height: 52px; background: var(--hospital-blue); }
  .hospital__name { font-size: 31px; font-weight: 700; color: var(--hospital-blue); }
  .hospital__address {
    position: absolute; left: 94px; top: 364px;
    font-size: 17px; color: var(--hospital-blue);
  }
  .languages {
    position: absolute; right: 30px; top: 340px;
    font-size: 20px; color: var(--ink);
  }
  .hours {
    position: absolute; right: 30px; top: 372px;
    font-size: 19px; color: var(--hours-orange);
  }
</style>
</head>
<body>

<section class="card card--back" aria-label="Reverso de la tarjeta">
  <div class="back__initials">MAQB</div>
  <div class="back__rule"></div>
  <div class="back__hospital">
    <span class="back__mark"></span>
    <span class="back__hospital-name">Hospital Almendral</span>
  </div>
  <div class="back__address">Calle Tomás Ibarrola #527 Col. Peñascal</div>
</section>

<section class="card card--front" aria-label="Frente de la tarjeta">
  <div class="front__band"></div>
  <div class="front__initials">MAQB</div>
  <div class="front__rule"></div>
  <div class="front__name">Dr. Mateo Anselmo Quiroga Benítez</div>
  <div class="front__specialty">Medicina general</div>

  <div class="contact">
    <div class="contact__row">
      <span class="contact__icon">
        <svg width="20" height="20" viewBox="0 0 24 24" aria-hidden="true">
          <path d="M6.6 10.8a15 15 0 0 0 6.6 6.6l2.2-2.2a1 1 0 0 1 1-.25 11.4 11.4 0 0 0 3.6.57 1 1 0 0 1 1 1V20a1 1 0 0 1-1 1A17 17 0 0 1 3 4a1 1 0 0 1 1-1h3.5a1 1 0 0 1 1 1c0 1.25.2 2.45.57 3.57a1 1 0 0 1-.25 1z" fill="#d8d51c"/>
        </svg>
      </span>
      <div>
        <div><span class="contact__label">Office</span>: 656-471-5836</div>
        <div><span class="contact__label">Emergency</span>: 613-907-5148</div>
      </div>
    </div>
    <div class="contact__row" style="margin-top:4px">
      <span class="contact__icon">
        <svg width="22" height="16" viewBox="0 0 22 16" aria-hidden="true">
          <rect x="1" y="1" width="20" height="14" fill="none" stroke="#d8d51c" stroke-width="2"/>
          <path d="M1 1l10 8 10-8" fill="none" stroke="#d8d51c" stroke-width="2"/>
        </svg>
      </span>
      <span>mateoqb@correoandino.net</span>
    </div>
  </div>

  <div class="hospital">
    <span class="hospital__mark"></span>
    <span class="hospital__name">Hospital Almendral</span>
  </div>
  <div class="hospital__address">Calle Tomás Ibarrola #527 Col. Peñascal</div>

  <div class="languages">English Spoken</div>
  <div class="hours">Sábado y domingo 10.00am a 10.00pm</div>
</section>

</body>
</html>
```